AI Startup Squarespace Website Design

I have a squarespace account setup with a domain name but need support to get the site looking good and launched. I will provide all text content and navigation/site map info. My company is working with clients to get business value out of Artificial Intelligence that helps automate processes, increase sales and improve customer customer experience. Leveraging the proven Q.Lumo AI Platform, our clients can get in-year benefits using customer service chatbots and other pre-built successful bots for automating/streamlining business processes in HR, accounting, underwriting, sales, training, remittances, emails, etc.

Target Market(s)

middle-market and large companies in Financial Services, Travel, Consumer Products, Manufacturing markets. Target is companies who want go improve sales, reduce costs and improve customer experience.

Industry/Entity Type

Financial

Font styles to use
Sans Serif

Requirements
Must have
• Professional but not too corporate-y.

```html
<!DOCTYPE html>
<html lang="en">
<head>
<meta charset="utf-8">
<title>Corvan — Artificial Intelligence that helps Automate Processes</title>
<link rel="stylesheet" href="https://fonts.googleapis.com/css2?family=Lato:ital,wght@0,300;0,400;0,700;1,400&family=Gelasio:ital@1&display=swap">
<style>
  :root {
    --ink: #2b2b2b;
    --muted: #5a5a5a;
    --soft: #7a7a7a;
    --brand-blue: #1a7cc4;
    --rule: #bdbdbd;
    --paper: #ffffff;
    --hero-deep: #031a36;
    --hero-mid: #0d3f78;
    --hero-glow: #4f9fe0;
  }
  * { box-sizing: border-box; margin: 0; padding: 0; }
  html, body { width: 765px; height: 1200px; overflow: hidden; background: var(--paper); }
  body { font-family: "Lato", Arial, sans-serif; color: var(--ink); position: relative; }

  .site-header { position: absolute; top: 0; left: 0; width: 765px; height: 61px; }
  .brand { position: absolute; left: 75px; top: 9px; display: flex; align-items: center; gap: 8px; }
  .brand-mark { width: 28px; height: 28px; background: var(--brand-blue); border-radius: 50%; }
  .brand-name { font-weight: 300; font-size: 34px; color: #8a8a8a; letter-spacing: 0.5px; line-height: 40px; }
  .main-nav { position: absolute; left: 268px; top: 26px; display: flex; gap: 12px; }
  .main-nav a { font-size: 8.6px; color: var(--muted); text-decoration: none; text-transform: uppercase; letter-spacing: 0.1px; }

  .hero { position: absolute; top: 61px; left: 0; width: 765px; height: 378px;
    background: radial-gradient(ellipse 230px 200px at 380px 150px, var(--hero-glow) 0%, var(--hero-mid) 45%, var(--hero-deep) 100%); }
  .hero-title { position: absolute; top: 143px; left: 0; width: 765px; text-align: center; color: #fff;
    font-weight: 400; font-size: 28px; line-height: 30px; }

  .welcome { position: absolute; top: 477px; left: 0; width: 765px; text-align: center; }
  .welcome h1 { font-weight: 400; font-size: 24px; line-height: 32px; color: var(--ink); }
  .welcome p { font-weight: 400; font-size: 18px; line-height: 26px; color: var(--muted); }

  .rule { position: absolute; left: 75px; width: 615px; height: 1px; background: var(--rule); }

  .feature { position: absolute; top: 622px; width: 200px; }
  .feature h2 { font-weight: 400; font-size: 14.5px; color: var(--brand-blue); line-height: 20px; margin-left: -3px; }
  .feature-photo { width: 189px; height: 141px; margin-top: 7px; }
  .feature p { margin-top: 18px; font-size: 8.6px; line-height: 14.5px; color: var(--muted); }
  .btn { display: inline-block; border: 1.5px solid var(--brand-blue); color: var(--brand-blue);
    font-size: 8.6px; text-transform: uppercase; text-decoration: none; text-align: center; letter-spacing: 0.2px; }
  .feature .btn { margin-top: 17px; width: 87px; height: 27px; line-height: 24px; }

  .testimonial { position: absolute; top: 976px; left: 75px; width: 420px; }
  .testimonial blockquote { font-family: "Gelasio", Georgia, serif; font-style: italic; font-size: 13.6px;
    line-height: 24px; color: var(--muted); }
  .testimonial .btn { margin-top: 13px; width: 126px; height: 27px; line-height: 24px; }

  .quick-links { position: absolute; top: 981px; left: 573px; }
  .quick-links h3 { font-weight: 400; font-size: 11px; color: var(--ink); line-height: 16px; margin-bottom: 5px; }
  .quick-links a { display: block; font-size: 9.2px; color: var(--soft); text-decoration: none; line-height: 19.5px; }

  .copyright { position: absolute; top: 1165px; left: 0; width: 765px; text-align: center; font-size: 9px; color: var(--muted); }
</style>
</head>
<body>
  <header class="site-header">
    <div class="brand"><span class="brand-mark"></span><span class="brand-name">corvan</span></div>
    <nav class="main-nav">
      <a href="#">Home</a><a href="#">About</a><a href="#">What We Do</a><a href="#">Our Technology</a>
      <a href="#">Problems We Solve</a><a href="#">News</a><a href="#">Contact</a>
    </nav>
  </header>

  <section class="hero" role="img" aria-label="Blue-toned digital artwork of artificial intelligence with a network of glowing lines">
    <h1 class="hero-title">Artificial Intelligence that helps<br>Automate Processes</h1>
  </section>

  <section class="welcome">
    <h1>Welcome to Corvan</h1>
    <p>Morbi diam mauris viverra in gravida eu mattis</p>
  </section>

  <div class="rule" style="top:577px"></div>

  <article class="feature" style="left:75px">
    <h2>What We Do</h2>
    <div class="feature-photo" role="img" aria-label="Audience seated at a business conference facing a presentation screen" style="background:linear-gradient(135deg,#e6e4e2,#8c8683 55%,#3c3a3a)"></div>
    <p>Morbi diam mauris viverra in gravida eu mattis in ante Morbi eget arcu Morbi porta libero id ullamcorper nonummy nibh ligula</p>
    <a class="btn" href="#">More Info</a>
  </article>

  <article class="feature" style="left:288px">
    <h2>Our Services</h2>
    <div class="feature-photo" role="img" aria-label="Glowing blue digital network forming a head shape on a dark background" style="background:radial-gradient(circle at 60% 50%,#2a8fd0 0%,#0b2a52 50%,#020c1c 100%)"></div>
    <p>Morbi diam mauris viverra in gravida eu mattis in ante Morbi eget arcu Morbi porta libero id ullamcorper nonummy nibh ligula</p>
    <a class="btn" href="#">More Info</a>
  </article>

  <article class="feature" style="left:500px">
    <h2>Why We Are</h2>
    <div class="feature-photo" role="img" aria-label="Two colleagues working together at a laptop in a bright office" style="background:linear-gradient(120deg,#c9b6a4,#eef1f3 55%,#dfe5ea)"></div>
    <p>Morbi diam mauris viverra in gravida eu mattis in ante Morbi eget arcu Morbi porta libero id ullamcorper nonummy nibh ligula</p>
    <a class="btn" href="#">More Info</a>
  </article>

  <div class="rule" style="top:950px"></div>

  <section class="testimonial">
    <blockquote>“Vivamus porttitor purus nisi eleifend libero a tempus libero lectus feugiat felis Morbi diam mauris viverra in gravida eu mattis in ante Morbi eget arcu Morbi porta libero id ullamcorper ”</blockquote>
    <a class="btn" href="#">Read Testimonial</a>
  </section>

  <nav class="quick-links">
    <h3>Quick Links</h3>
    <a href="#">Home</a><a href="#">About</a><a href="#">What We Do</a><a href="#">Our Technology</a>
    <a href="#">Problems We Solve</a><a href="#">News</a><a href="#">Contact</a>
  </nav>

  <div class="rule" style="top:1152px"></div>

  <footer class="copyright">© 2018 Company Name &nbsp;All right reserved</footer>
</body>
</html>
```